A start up Private Wine Label for export to Asia.

We are looking for the best graphic design for our very first wine label Corvessa Vineyards and would like the following requirements:

1. Black background - explore and play around the shade of black
2. Gold Shimmery Colour Font
3. Font should be a cursive classic posh that says Corvessa Vineyards
4. We would like the front graphic design to be simple and elegant and has a traditional classic feel to it.

Target Market(s)

Small scale to test the upper class market for export to Asia

Font styles to use
Script

Colors

Designer to choose colors to be used in the design.

Requirements
Must have
• Gold font for the label Corvessa Vineyards with shimmery touch to it.
• Elegant black background.
• Simple but elegant design.
• Attractive to the upper class market in Asia.
Nice to have
• Explore and play around with your imagination.

```html
<!DOCTYPE html>
<html lang="en">
<head>
<meta charset="utf-8">
<title>Corvessa Vineyards – Pinot Noir Label</title>
<link href="https://fonts.googleapis.com/css2?family=Pinyon+Script&family=Lato:wght@700&display=swap" rel="stylesheet">
<style>
  :root {
    --backdrop: #d3cbc2;
    --backdrop-light: #e4ddd6;
    --label-black: #1c1c1d;
    --label-mid: #343436;
    --gold: #d6ae57;
    --gold-light: #efd48a;
    --gold-deep: #a97c2c;
    --ink-white: #f4f2ee;
  }
  html, body {
    margin: 0;
    padding: 0;
    width: 1200px;
    height: 900px;
    overflow: hidden;
  }
  body {
    background: radial-gradient(ellipse at 40% 45%, var(--backdrop-light) 0%, var(--backdrop) 75%);
    position: relative;
  }
  .wine-label {
    position: absolute;
    left: 404px;
    top: 61px;
    width: 392px;
    height: 778px;
  }
  .label-shape {
    position: absolute;
    inset: 0;
  }
  .ornament {
    position: absolute;
    left: 50%;
    transform: translateX(-50%);
    border-radius: 50%;
  }
  .ornament-top {
    top: 14px;
    width: 272px;
    height: 190px;
    background: radial-gradient(ellipse at center, rgba(214,174,87,0.55) 0%, rgba(214,174,87,0.18) 55%, rgba(214,174,87,0) 72%);
  }
  .ornament-bottom {
    top: 702px;
    width: 272px;
    height: 56px;
    background: radial-gradient(ellipse at center, rgba(214,174,87,0.5) 0%, rgba(214,174,87,0.15) 55%, rgba(214,174,87,0) 72%);
  }
  .brand-name {
    position: absolute;
    left: 0;
    right: 0;
    top: 250px;
    margin: 0;
    text-align: center;
    font-family: "Pinyon Script", cursive;
    font-weight: 400;
    color: var(--gold);
    line-height: 1;
  }
  .brand-name span {
    display: block;
  }
  .brand-line-one {
    font-size: 78px;
  }
  .brand-line-two {
    font-size: 66px;
    margin-top: 8px;
  }
  .varietal {
    position: absolute;
    left: 0;
    right: 0;
    top: 520px;
    margin: 0;
    text-align: center;
    font-family: "Lato", sans-serif;
    font-weight: 700;
    font-size: 29px;
    letter-spacing: 0.5px;
    color: var(--ink-white);
  }
  .divider {
    position: absolute;
    left: 36px;
    width: 320px;
    top: 561px;
    height: 14px;
  }
  .vintage {
    position: absolute;
    left: 0;
    right: 0;
    top: 585px;
    margin: 0;
    text-align: center;
    font-family: "Lato", sans-serif;
    font-weight: 700;
    font-size: 23px;
    color: var(--ink-white);
  }
  .rating {
    position: absolute;
    left: 50%;
    transform: translateX(-50%);
    top: 645px;
    width: 112px;
    height: 40px;
  }
</style>
</head>
<body>
  <main class="wine-label">
    <svg class="label-shape" viewBox="0 0 392 778" width="392" height="778" aria-hidden="true">
      <defs>
        <linearGradient id="labelShade" x1="0" y1="0" x2="1" y2="0">
          <stop offset="0" stop-color="var(--label-black)"/>
          <stop offset="0.5" stop-color="var(--label-mid)"/>
          <stop offset="1" stop-color="var(--label-black)"/>
        </linearGradient>
      </defs>
      <path d="M30 0 H362 A30 30 0 0 0 392 30 V748 A30 30 0 0 0 362 778 H30 A30 30 0 0 0 0 748 V30 A30 30 0 0 0 30 0 Z" fill="url(#labelShade)"/>
    </svg>

    <div class="ornament ornament-top" role="img" aria-label="Gold calligraphic flourish ornament"></div>

    <h1 class="brand-name">
      <span class="brand-line-one">Corvessa</span>
      <span class="brand-line-two">Vineyards</span>
    </h1>

    <p class="varietal">PINOT NOIR</p>

    <svg class="divider" viewBox="0 0 320 14" aria-hidden="true">
      <line x1="6" y1="7" x2="116" y2="7" stroke="var(--gold)" stroke-width="1.6"/>
      <line x1="204" y1="7" x2="314" y2="7" stroke="var(--gold)" stroke-width="1.6"/>
      <path d="M0 7 L6 3 L12 7 L6 11 Z" fill="var(--gold)"/>
      <path d="M308 7 L314 3 L320 7 L314 11 Z" fill="var(--gold)"/>
    </svg>

    <p class="vintage">2019</p>

    <svg class="rating" viewBox="0 0 112 40" aria-label="Five glass rating" role="img">
      <g fill="var(--gold)">
        <path id="glass" d="M2 0 H18 C18 12 14 17 11 18 V34 H16 V37 H4 V34 H9 V18 C6 17 2 12 2 0 Z"/>
        <use href="#glass" x="23"/>
        <use href="#glass" x="46"/>
        <use href="#glass" x="69"/>
        <use href="#glass" x="92"/>
      </g>
    </svg>

    <div class="ornament ornament-bottom" role="img" aria-label="Gold calligraphic scroll ornament"></div>
  </main>
</body>
</html>
```